residential/commercial designer. looking to expand customer base.

we need a postcard design for an established residential/commercial interior design firm. TRV Interiors has over 25 yrs experience in creating unique and timeless residential and commercial spaces. offering assistance with cabinet design & furniture, accessories, lighting, plumbing & finish selections in new construction and renovation projects. TRV Interiors has completed projects in New York, California, Florida and Arizona. we will work with clients builder and them to create their personal space. this allows project to progress smoothly and cost effectively.
want postcard simple, straight forward architectural design concept. not whimsical. maybe wanting to incorporate a tag line.
don't expect to include all photos on postcard. looking to your expert opinion on which words and photos should be included on postcard. i know i don't need to say "i want a design that people don't throw away when they receive it"
include: TRV Interiors, Unified Spaces, info@trvinteriorsdemo.com, 555-314-9082 , Maren Dovetti, Principal
please contact me with your questions
Target Market(s)
high end residential, high style commercial
Industry/Entity Type
Residential
Requirements
Must have
- TRV Interior
- Unified Spaces
- info@trvinteriorsdemo.com
- 555-314-9082
- Maren Dovetti, Principal
- best photos with most visual impact.
- use different photos to show design diversity and style
Nice to have
- tag line

```html
<!DOCTYPE html>
<html lang="en">
<head>
<meta charset="utf-8">
<title>TRV Interiors Postcard</title>
<link rel="stylesheet" href="https://fonts.googleapis.com/css2?family=Oswald:wght@300;400&family=Parisienne&display=swap">
<style>
  :root {
    --page-bg: #ecebe8;
    --blue-deep: #2473c2;
    --blue-mid: #5b9ddb;
    --blue-pale: #c4dcf2;
    --wall-warm: #cfc2a2;
    --wall-shadow: #a89a7c;
    --shelf-white: #fbf9f3;
    --shelf-shade: #e4ded0;
    --book-dark: #4a4038;
    --floor-brown: #5e4632;
    --logo-brown: #5a3f2e;
    --text-light: #ffffff;
    --quote-blue: #2a7ccc;
  }
  * { margin: 0; padding: 0; box-sizing: border-box; }
  html, body {
    width: 1200px;
    height: 772px;
    overflow: hidden;
    background: var(--page-bg);
  }
  .postcard {
    position: absolute;
    left: 31px;
    top: 31px;
    width: 1138px;
    height: 709px;
    overflow: hidden;
    box-shadow: 0 4px 14px rgba(0,0,0,0.25);
  }
  .room-photo {
    position: absolute;
    inset: 0;
    background:
      radial-gradient(ellipse 180px 120px at 720px 640px, rgba(74,58,44,0.85), rgba(74,58,44,0) 100%),
      radial-gradient(ellipse 260px 90px at 640px 700px, rgba(94,70,50,0.9), rgba(94,70,50,0) 100%),
      radial-gradient(ellipse 110px 200px at 900px 340px, rgba(74,64,56,0.45), rgba(74,64,56,0) 100%),
      radial-gradient(ellipse 90px 160px at 640px 320px, rgba(74,64,56,0.35), rgba(74,64,56,0) 100%),
      radial-gradient(ellipse 230px 330px at 930px 360px, var(--shelf-white), rgba(251,249,243,0) 100%),
      radial-gradient(ellipse 180px 280px at 640px 380px, var(--shelf-white), rgba(251,249,243,0) 100%),
      radial-gradient(ellipse 280px 140px at 690px 90px, var(--wall-warm), rgba(207,194,162,0) 100%),
      radial-gradient(ellipse 120px 260px at 780px 420px, var(--wall-shadow), rgba(168,154,124,0) 100%),
      linear-gradient(180deg, var(--shelf-shade) 0%, var(--wall-warm) 25%, var(--shelf-shade) 55%, var(--wall-warm) 82%, var(--floor-brown) 100%);
  }
  .blue-panel {
    position: absolute;
    inset: 0;
    background: linear-gradient(90deg,
      var(--blue-deep) 0%,
      var(--blue-mid) 20%,
      var(--blue-pale) 36%,
      rgba(196,220,242,0.65) 43%,
      rgba(196,220,242,0) 52%);
  }
  .rule {
    position: absolute;
    left: 117px;
    width: 269px;
    height: 1px;
    background: rgba(255,255,255,0.85);
  }
  .rule--top { top: 44px; }
  .rule--bottom { top: 659px; }
  .verse {
    position: absolute;
    left: 0;
    top: 0;
    width: 546px;
    font-family: "Oswald", sans-serif;
    font-weight: 300;
    font-size: 24px;
    color: var(--text-light);
    text-align: center;
  }
  .verse__line {
    position: absolute;
    left: 0;
    width: 100%;
    line-height: 1;
  }
  .quote-mark {
    font-family: "Oswald", sans-serif;
    font-weight: 400;
    font-size: 64px;
    color: var(--quote-blue);
    line-height: 0;
    vertical-align: -22px;
  }
  .brand-box {
    position: absolute;
    left: 898px;
    top: 44px;
    width: 196px;
    height: 154px;
    background: var(--logo-brown);
    border: 2px solid var(--text-light);
    color: var(--text-light);
    text-align: center;
    font-family: "Oswald", sans-serif;
    font-weight: 300;
  }
  .brand-box__name {
    margin-top: 26px;
    font-size: 32px;
    line-height: 1.1;
  }
  .brand-box__tagline {
    margin-top: 12px;
    font-size: 14px;
    letter-spacing: 1px;
  }
  .signature {
    position: absolute;
    right: 30px;
    top: 578px;
    font-family: "Parisienne", cursive;
    font-size: 29px;
    color: var(--text-light);
  }
  .contact-rule {
    position: absolute;
    left: 562px;
    top: 628px;
    width: 576px;
    height: 1px;
    background: rgba(255,255,255,0.85);
  }
  .contact {
    position: absolute;
    top: 652px;
    font-family: "Oswald", sans-serif;
    font-weight: 300;
    color: var(--text-light);
  }
  .contact--email { left: 562px; font-size: 16px; letter-spacing: 4px; }
  .contact--phone { right: 30px; top: 648px; font-size: 19px; letter-spacing: 4px; }
</style>
</head>
<body>
  <main class="postcard">
    <div class="room-photo" role="img" aria-label="Photograph of a home library with white built-in bookshelves around an archway, filled with books, and a globe on a stand"></div>
    <div class="blue-panel"></div>

    <div class="rule rule--top"></div>
    <div class="verse">
      <p class="verse__line" style="top:112px"><span class="quote-mark">&ldquo;</span> Dreams crafted,</p>
      <p class="verse__line" style="top:190px">With a vision to inspire,</p>
      <p class="verse__line" style="top:266px">Indulge and imagine,</p>
      <p class="verse__line" style="top:343px">To create a world within&hellip;</p>
      <p class="verse__line" style="top:416px">That is serene than the outer one!</p>
      <p class="verse__line" style="top:492px">Dreams crafted,</p>
      <p class="verse__line" style="top:569px">For tenure called life! <span class="quote-mark">&rdquo;</span></p>
    </div>
    <div class="rule rule--bottom"></div>

    <div class="brand-box">
      <p class="brand-box__name">TRV<br>Interiors</p>
      <p class="brand-box__tagline">Unified Spaces</p>
    </div>

    <p class="signature">Maren Dovetti, Principal</p>
    <div class="contact-rule"></div>
    <p class="contact contact--email">info@trvinteriorsdemo.com</p>
    <p class="contact contact--phone">555-314-9082</p>
  </main>
</body>
</html>
```